Creative & Professional Business Card for hair salon

We are looking to update our business cards. Our salon is creative, modern, progressive and professional and looking for a design that will reflect this.

```html
<!DOCTYPE html>
<html lang="en">
<head>
<meta charset="utf-8">
<title>Velvet Loft – Business Card</title>
<link href="https://fonts.googleapis.com/css2?family=Open+Sans:wght@400;600;700&display=swap" rel="stylesheet">
<style>
  :root {
    --backdrop: #3b3431;
    --card: #151618;
    --accent: #7fb4c6;
    --text: #f1f1f1;
    --muted: #8a8d91;
    --rule: #4f7f90;
  }
  * { margin: 0; padding: 0; box-sizing: border-box; }
  html, body {
    width: 1200px; height: 864px; overflow: hidden;
    background: var(--backdrop);
    font-family: "Open Sans", Arial, sans-serif;
  }
  .canvas { position: relative; width: 1200px; height: 864px; }
  .card {
    position: absolute; top: 282px;
    width: 520px; height: 300px;
    background: var(--card);
    border-radius: 3px;
    color: var(--text);
  }
  .card--back { left: 50px; }
  .card--front { left: 630px; }

  /* back */
  .back-brand {
    position: absolute; top: 112px; left: 0; right: 0;
    text-align: center;
    font-size: 34px; font-weight: 400; letter-spacing: 1px;
    color: #c9cbce;
  }
  .back-web {
    position: absolute; top: 178px; left: 0; right: 0;
    text-align: center;
    font-size: 12px; letter-spacing: 2.5px; color: var(--muted);
  }

  /* front */
  .person { position: absolute; left: 34px; top: 128px; }
  .person__name { font-size: 16px; font-weight: 700; color: var(--accent); letter-spacing: .5px; }
  .person__title { font-size: 10.5px; color: var(--accent); letter-spacing: .5px; margin-top: -2px; }
  .contacts { position: absolute; left: 34px; top: 180px; list-style: none; }
  .contacts li {
    display: flex; align-items: center; gap: 8px;
    font-size: 12.5px; line-height: 20px; color: var(--text);
  }
  .contacts svg { width: 11px; height: 11px; flex: none; }
  .brand { position: absolute; right: 30px; top: 120px; text-align: right; }
  .brand__name { font-size: 22px; font-weight: 400; color: var(--accent); }
  .brand__by { font-size: 11px; color: var(--accent); margin-top: 2px; }
  .rule {
    position: absolute; left: 34px; right: 30px; top: 238px;
    height: 1px; background: var(--rule);
  }
  .rule--short { top: 170px; right: 330px; }
  .address {
    position: absolute; right: 30px; top: 250px;
    text-align: right; font-size: 13px; font-weight: 600; line-height: 18px;
  }
</style>
</head>
<body>
<main class="canvas">
  <section class="card card--back">
    <p class="back-brand">Velvet Loft</p>
    <p class="back-web">www.velvetloft.com.ac</p>
  </section>

  <section class="card card--front">
    <div class="person">
      <p class="person__name">LIAM HART</p>
      <p class="person__title">PRESIDENT</p>
    </div>
    <div class="rule rule--short"></div>
    <ul class="contacts">
      <li>
        <svg viewBox="0 0 12 12" aria-hidden="true"><path d="M2 1h3l1 3-1.5 1a6 6 0 0 0 2.5 2.5L8 6l3 1v3a1 1 0 0 1-1 1A9 9 0 0 1 1 2a1 1 0 0 1 1-1z" fill="var(--muted)"/></svg>
        07 5400 2817
      </li>
      <li>
        <svg viewBox="0 0 12 12" aria-hidden="true"><rect x="1" y="2.5" width="10" height="7" rx="1" fill="var(--muted)"/><path d="M1.5 3l4.5 3.5L10.5 3" stroke="var(--card)" fill="none"/></svg>
        salon@velvetloft.com.ac
      </li>
      <li>
        <svg viewBox="0 0 12 12" aria-hidden="true"><circle cx="6" cy="6" r="5" fill="var(--muted)"/></svg>
        VelvetLoftbyMiaCorso
      </li>
    </ul>
    <div class="brand">
      <p class="brand__name">Velvet Loft</p>
      <p class="brand__by">by Mia Corso</p>
    </div>
    <div class="rule"></div>
    <p class="address">12/40 Harbour Lane, Noosa<br>www.velvetloft.com.ac</p>
  </section>
</main>
</body>
</html>
```